Design for Card Attached to Clothes

We sell rhythmic gymnastics apparel and are looking for someone create a card that will be attached to the products. You can see an example of the exact type of apparel in the files, as well as the current card that is attached to it. The design should have space on the top back for the sticker that has UPC and SKU information, as shown in the image attached.
- We would like the front to have our logo
- We would like the image of the girls added on the back
- Would be cool to see the gradient change to the white space on the back where the sticker will go but not required.
-The final card size is 10cm by 6cm, Their should be 2mm loss accounted for cutting the cards within the design. (meaning the design needs to be bigger than 10cm by 6cm to account for printing and cut)
- And the hole size that is at the top center is 3mm in diameter
- Name should be under logo
Access all logo files here https://files.plomvarek.net/share/folders/7Kq2TzWm9RbXa4LpYc8NdVe3Hs5JfGu1?view=open
- Front will have logo
- Back will have image of girls and some creative design that you will create.
Females
Rhythmic Gymnastics

```html
<!DOCTYPE html>
<html lang="en">
<head>
<meta charset="UTF-8">
<title>Design for Card Attached to Clothes</title>
<link rel="stylesheet" href="https://fonts.googleapis.com/css2?family=Figtree:wght@400;500&family=Quicksand:wght@500&display=swap">
<style>
  :root {
    --board: #cacaca;
    --ink: #1a1a1a;
    --white: #ffffff;
    --plum: #a3318f;
    --magenta: #e5136f;
    --orchid: #b8449a;
    --rose: #df2a7d;
    --berry: #b02e8e;
    --raspberry: #dc2a6e;
    --edge-pink: #e0358a;
    --photo-dark: #2a2228;
    --photo-mid: #6b4a5c;
  }
  * { margin: 0; padding: 0; box-sizing: border-box; }
  html, body { width: 1200px; height: 3125px; overflow: hidden; }
  body {
    background: var(--board);
    position: relative;
    font-family: "Figtree", Arial, sans-serif;
    color: var(--ink);
  }
  .board-title {
    position: absolute; top: 52px; left: 0; width: 1200px;
    text-align: center; font-size: 41px; font-weight: 400; letter-spacing: 0.5px;
  }
  .sample-label {
    position: absolute; left: 0; width: 1166px;
    text-align: center; font-size: 19px; font-weight: 400;
  }
  .tag {
    position: absolute; width: 475px; height: 790px; overflow: hidden;
    box-shadow: 1px 2px 3px rgba(0,0,0,0.35);
  }
  .tag--left { left: 93px; }
  .tag--right { left: 624px; }
  .hole {
    position: absolute; top: 56px; left: 50%; width: 17px; height: 17px;
    margin-left: -8.5px; border-radius: 50%;
    background: radial-gradient(circle at 40% 35%, #e2e2e2, #9a9a9a);
    box-shadow: inset 0 1px 2px rgba(0,0,0,0.4); z-index: 5;
  }
  .grad-front { background: linear-gradient(170deg, var(--plum) 0%, #c9227f 55%, var(--magenta) 100%); }
  .grad-back-soft { background: linear-gradient(175deg, var(--orchid) 0%, #cf3189 50%, var(--rose) 100%); }
  .grad-back-deep { background: linear-gradient(175deg, var(--berry) 0%, #c52a84 50%, var(--raspberry) 100%); }
  .tag--plain-white { background: var(--white); }
  .soft-sheen {
    position: absolute; right: -180px; top: 180px; width: 560px; height: 700px;
    border-radius: 50%; background: rgba(255,255,255,0.06);
  }
  .wordmark {
    position: absolute; left: 0; width: 100%;
    display: flex; align-items: center; justify-content: center; gap: 22px;
    font-family: "Quicksand", Arial, sans-serif; font-weight: 500;
    font-size: 104px; line-height: 1; color: var(--white);
  }
  .wordmark__dot { width: 44px; height: 44px; border-radius: 50%; background: var(--white); }
  .wordmark--magenta { color: var(--magenta); font-size: 90px; }
  .wordmark--magenta .wordmark__dot { background: var(--magenta); width: 38px; height: 38px; }
  .shape-layer { position: absolute; left: 0; top: 0; }
  .photo {
    position: absolute; border-radius: 40px;
    background: linear-gradient(180deg, var(--photo-mid) 0%, var(--photo-dark) 100%);
    opacity: 0.55;
  }
</style>
</head>
<body>
  <h1 class="board-title">Design for Card Attached to Clothes</h1>

  <!-- Sample 1 -->
  <p class="sample-label" style="top:154px;">SAMPLE 1</p>
  <section class="tag tag--left grad-front" style="top:210px;">
    <div class="soft-sheen"></div>
    <span class="hole"></span>
    <div class="wordmark" style="top:440px;"><span class="wordmark__dot"></span>Velora</div>
  </section>
  <section class="tag tag--right grad-back-soft" style="top:210px;">
    <div class="soft-sheen"></div>
    <span class="hole"></span>
    <div class="photo" role="img" aria-label="Two gymnasts in black leotards seated in a back-bend stretch, arms raised" style="left:32px; top:427px; width:428px; height:346px;"></div>
  </section>

  <!-- Sample 2 -->
  <p class="sample-label" style="top:1106px;">SAMPLE 2</p>
  <section class="tag tag--left grad-front" style="top:1173px;">
    <span class="hole"></span>
    <div class="wordmark" style="top:440px;"><span class="wordmark__dot"></span>Velora</div>
  </section>
  <section class="tag tag--right grad-front" style="top:1173px;">
    <svg class="shape-layer" width="475" height="790" viewBox="0 0 475 790" aria-hidden="true">
      <path d="M0 0 H475 V215 C430 370 330 420 220 430 C110 440 40 480 0 600 Z" fill="var(--white)"/>
      <path d="M475 215 C430 370 330 420 220 430 C110 440 40 480 0 600" fill="none" stroke="var(--edge-pink)" stroke-width="12"/>
      <rect x="0" y="774" width="475" height="16" fill="var(--magenta)" opacity="0.6"/>
    </svg>
    <span class="hole"></span>
    <div class="photo" role="img" aria-label="Two gymnasts in black leotards standing side by side" style="left:38px; top:323px; width:200px; height:391px;"></div>
    <div class="photo" role="img" aria-label="Two gymnasts in black leotards seated in a back-bend stretch" style="left:144px; top:473px; width:330px; height:301px;"></div>
  </section>

  <!-- Sample 3 -->
  <p class="sample-label" style="top:2068px;">SAMPLE 3</p>
  <section class="tag tag--left grad-front" style="top:2139px;">
    <svg class="shape-layer" width="475" height="790" viewBox="0 0 475 790" aria-hidden="true">
      <path d="M0 0 H475 V491 Q237 647 0 491 Z" fill="var(--white)"/>
    </svg>
    <span class="hole"></span>
    <div class="wordmark wordmark--magenta" style="top:340px;"><span class="wordmark__dot"></span>Velora</div>
    <div class="photo" role="img" aria-label="Two gymnasts in black leotards seated in a back-bend stretch, arms raised" style="left:58px; top:459px; width:372px; height:306px;"></div>
  </section>
  <section class="tag tag--right grad-back-deep" style="top:2139px;">
    <div class="soft-sheen"></div>
    <span class="hole"></span>
    <div class="photo" role="img" aria-label="Two gymnasts in black leotards standing side by side" style="left:126px; top:318px; width:223px; height:437px;"></div>
  </section>
</body>
</html>
```